Restoration Specialist in need of business card designs

One side of the business card is a bathroom ripped out down to the studs with just a sink and toilet and then the other side is the bathroom (same sink and toilet) but put back together. Like a before and after on each side behind our information. Stand out, hard to forget, business cards for my restoration company. I want a unique concept all together.
Must include in no particular order:
our business name "Summit Renewals"
Possible Logo for a restoration company
Owner; Dennis Moravec
410-386-7294
dmoravec@summitrenewalsqx.example
SummitRenewalsQX.example (our company website) BUT I am open to any and all designs and options.

Target Market(s)

Customers, Men in the mitigation, plumbing, electrical, HVAC, Roofing, insurance companies

Industry/Entity Type

Restoration/ construction

Contact Information for Business Card

Must include in no particular order: our business name "Summit Renewals" Owner; Dennis Moravec 410-386-7294 dmoravec@summitrenewalsqx.example SummitRenewalsQX.example (our company website) MAY include a list of our services: Residential~ Emergency Response ~ Board- up~ Complete Restoration

Font styles to use
Serif

Colors
0054AA
0677BA
7BADD7
CADEEF
E8F1F8
F0912C
F2A743
F7CA91
FBE8D2
FDF5EE

Requirements
Must have
• unique, memorable, not something men have seen over and over again,
Nice to have
• eye catching
Should not have
• Been something I could have made by myself

```html
<!DOCTYPE html>
<html lang="en">
<head>
<meta charset="utf-8">
<title>Summit Renewals — Business Card</title>
<link href="https://fonts.googleapis.com/css2?family=Playfair+Display:wght@400;700&display=swap" rel="stylesheet">
<style>
  :root {
    --backdrop: #cfd5d5;
    --card-white: #f2f2f0;
    --brand-orange: #e5681c;
    --brand-navy: #17344f;
    --ink: #2b2b2b;
    --on-orange: #f6f3ef;
  }
  * { box-sizing: border-box; margin: 0; padding: 0; }
  html, body { width: 1200px; height: 881px; overflow: hidden; }
  body {
    background: var(--backdrop);
    font-family: "Playfair Display", Georgia, serif;
    position: relative;
  }
  .card {
    position: absolute;
    width: 525px;
    height: 300px;
    box-shadow: 0 18px 40px rgba(0,0,0,0.18);
  }
  .card--front { left: 50px; top: 290px; background: var(--card-white); border-bottom: 3px solid var(--brand-orange); }
  .card--back { left: 625px; top: 290px; background: var(--brand-orange); display: flex; align-items: center; justify-content: center; }

  .brand-name {
    position: absolute; left: 38px; top: 70px; width: 190px;
    color: var(--brand-navy); font-weight: 700; font-size: 34px; line-height: 1.05;
    text-align: center;
  }
  .brand-name .brand-square {
    display: block; width: 14px; height: 14px; margin: 0 auto 10px;
    background: var(--brand-orange);
  }
  .divider-vertical {
    position: absolute; left: 250px; top: 40px; width: 2px; height: 150px;
    background: var(--brand-orange);
  }
  .contact { position: absolute; left: 272px; top: 44px; }
  .contact__name { color: var(--brand-orange); font-weight: 700; font-size: 27px; line-height: 1.1; }
  .contact__role { color: var(--brand-navy); font-size: 14px; margin-top: 2px; }
  .contact__rule { width: 48px; height: 2px; background: var(--brand-orange); margin: 12px 0 12px; }
  .contact__list { list-style: none; }
  .contact__list li {
    display: flex; align-items: center; gap: 8px;
    font-size: 12px; color: var(--ink); line-height: 1.9;
  }
  .contact__list svg { width: 11px; height: 11px; fill: var(--brand-orange); flex: none; }

  .services { position: absolute; left: 28px; right: 28px; bottom: 20px; text-align: center; }
  .services__heading {
    display: flex; align-items: center; gap: 12px;
    color: var(--brand-orange); font-weight: 700; font-size: 19px;
  }
  .services__heading::before, .services__heading::after {
    content: ""; flex: 1; height: 1.5px; background: var(--brand-orange);
  }
  .services__list { font-size: 11.5px; color: var(--ink); margin-top: 6px; letter-spacing: 0.1px; }

  .back-brand {
    color: var(--on-orange); font-weight: 700; font-size: 48px; line-height: 1.05;
    text-align: center;
  }
  .back-brand .brand-square {
    display: block; width: 20px; height: 20px; margin: 0 auto 14px;
    background: var(--on-orange);
  }
</style>
</head>
<body>

<section class="card card--front" aria-label="Business card front">
  <div class="brand-name"><span class="brand-square"></span>Summit<br>Renewals</div>
  <div class="divider-vertical"></div>

  <div class="contact">
    <div class="contact__name">Dennis Moravec</div>
    <div class="contact__role">Owner</div>
    <div class="contact__rule"></div>
    <ul class="contact__list">
      <li>
        <svg viewBox="0 0 24 24" aria-hidden="true"><path d="M6.6 10.8a15.1 15.1 0 0 0 6.6 6.6l2.2-2.2c.3-.3.7-.4 1-.2 1.1.4 2.3.6 3.6.6.6 0 1 .4 1 1V20c0 .6-.4 1-1 1A17 17 0 0 1 3 4c0-.6.4-1 1-1h3.5c.6 0 1 .4 1 1 0 1.3.2 2.5.6 3.6.1.3 0 .7-.2 1z"/></svg>
        410-386-7294
      </li>
      <li>
        <svg viewBox="0 0 24 24" aria-hidden="true"><path d="M2 5h20v14H2z M2 5l10 8 10-8" fill="var(--brand-orange)"/><path d="M3 6l9 7 9-7" stroke="#fff" stroke-width="1.6" fill="none"/></svg>
        dmoravec@summitrenewalsqx.example
      </li>
      <li>
        <svg viewBox="0 0 24 24" aria-hidden="true"><circle cx="12" cy="12" r="10"/><path d="M2 12h20M12 2c3 3 3 17 0 20M12 2c-3 3-3 17 0 20" stroke="#fff" stroke-width="1.4" fill="none"/></svg>
        SummitRenewalsQX.example
      </li>
    </ul>
  </div>

  <div class="services">
    <div class="services__heading">Services</div>
    <div class="services__list">Residential~ Emergency Response ~ Board- up~ Storm Protection~ Complete Restoration</div>
  </div>
</section>

<section class="card card--back" aria-label="Business card back">
  <div class="back-brand"><span class="brand-square"></span>Summit<br>Renewals</div>
</section>

</body>
</html>
```